Bold Cover needed for a book on Workplace Bullying

I need a book cover design for a book titled, “Iron Silence?” The book recounts my story of bullying in the workplace. It also includes chapters on how readers can minimize/stop workplace bullying, write an effective complaint, and ensure their own mental wellbeing.
I am looking for a bold design using red and black, and possibly distressed lettering. The covers of other books dealing with this subject do not reflect my vision. They are often too childish or look too academic. This book needs to stress the serious nature of a toxic workplace, while appealing to readers experiencing a similar situation. I’d like the cover to reflect the mental anguish associated with workplace bullying (hence the distressed lettering).
I have included a cover that appeals to me (although the coloring is wrong). That said, I am also very happy (and excited) to see your creative input!
On the cover, it should have the following:
Title: Iron Silence?
Subtitle: How the Harbour Works Department Condones Bullying & Ruins Lives
Author: Owen Frick
Other relevant details:
Book size: 5.5” x 8.5”
Back cover will have a blurb, author picture/short bio, and barcode
The blurb on the back cover reads:
Undermining, intimidation and threats
Despite the Department of Harbour Works allegedly holding a zero tolerance for bullying, these behaviours were an everyday occurrence in at least one workplace. Even after a decade of complaints, numerous witnesses and physical proof, the department failed to act. Instead, they looked the other way, allowing one powerful and well-connected individual to end careers and ruin lives.
After being targeted, one teacher resolved to put an end to the abuse experienced by more than fifty employees. His startling story reveals the relentless bullying, mental health ramifications, and insidious tactics used to cover up the corrosive behaviour.
Those who have experienced a toxic workplace will also find much needed support and guidance, intended to minimise suffering and detail a clear way forward. Chapters include dealing with bullying in the workplace, how to lodge a successful complaint, and how to stay sane during any potential legal action.

```html
<!DOCTYPE html>
<html lang="en">
<head>
<meta charset="utf-8">
<title>Iron Silence? – Cover Wrap</title>
<link href="https://fonts.googleapis.com/css2?family=Rubik+Dirt&family=Arimo:wght@400&display=swap" rel="stylesheet">
<style>
  :root {
    --backdrop: #2b2b2b;
    --paper: #ffffff;
    --ink: #111111;
    --accent: #c8141c;
    --art-tone: #e6e6e6;
  }
  * { box-sizing: border-box; margin: 0; padding: 0; }
  html, body {
    width: 1200px; height: 1200px; overflow: hidden;
    background: var(--backdrop);
  }
  .wrap {
    position: absolute; left: 20px; top: 177px;
    width: 1160px; height: 846px; overflow: hidden;
    background: var(--paper); color: var(--ink);
    font-family: "Arimo", Arial, sans-serif;
  }
  .distressed {
    font-family: "Rubik Dirt", "Impact", sans-serif;
    font-weight: 400;
    color: var(--ink);
    text-shadow: 3px 3px 0 var(--accent);
    line-height: 1;
    white-space: nowrap;
  }

  /* back cover */
  .back { position: absolute; left: 57px; top: 0; width: 434px; }
  .back-title {
    position: absolute; left: 0; top: 46px; width: 100%;
    text-align: center; font-size: 40px;
  }
  .back-subtitle {
    position: absolute; left: 0; top: 95px; width: 100%;
    text-align: center; font-size: 20px; line-height: 31px;
  }
  .blurb { position: absolute; left: 0; top: 170px; width: 100%; }
  .blurb p { font-size: 15px; line-height: 22px; text-align: justify; }
  .blurb p + p { margin-top: 22px; }

  /* spine */
  .spine-title {
    position: absolute; left: 558px; top: 46px;
    writing-mode: vertical-rl; font-size: 38px;
  }
  .spine-author {
    position: absolute; left: 568px; top: 623px;
    writing-mode: vertical-rl; font-size: 26px; line-height: 1; letter-spacing: 0.5px;
  }

  /* front cover */
  .front { position: absolute; left: 607px; top: 0; width: 553px; height: 846px; text-align: center; }
  .front-title { position: absolute; left: 0; top: 34px; width: 100%; }
  .front-title-line1 { display: block; font-size: 112px; text-shadow: 5px 5px 0 var(--accent); }
  .front-title-line2 { display: block; margin-top: 4px; font-size: 84px; text-shadow: 5px 5px 0 var(--accent); }
  .cover-art {
    position: absolute; left: 45px; top: 252px; width: 464px; height: 424px;
    background: radial-gradient(ellipse at 50% 40%, #f5f5f5, var(--art-tone));
  }
  .ground-line {
    position: absolute; left: 45px; top: 676px; width: 464px; height: 1px; background: var(--ink);
  }
  .front-subtitle {
    position: absolute; left: 0; top: 696px; width: 100%;
    font-size: 20px; line-height: 31px;
  }
  .front-author {
    position: absolute; left: 0; top: 782px; width: 100%;
    font-size: 34px; line-height: 1; letter-spacing: 0.5px;
  }
</style>
</head>
<body>
  <main class="wrap">
    <section class="back">
      <h2 class="back-title distressed">Iron Silence?</h2>
      <p class="back-subtitle">How the Harbour Works Department Condones<br>Bullying &amp; Ruins Lives</p>
      <div class="blurb">
        <p>Lorem ipsum dolor sit amet, consectetur adipiscing elit, sed do eiusmod tempor incididunt ut labore et dolore magna aliqua. Quis ipsum suspendisse ultrices gravida. Risus commodo viverra maecenas accumsan lacus vel facilisis. Lorem ipsum dolor sit amet, consectetur adipiscing elit, sed do eiusmod tempor incididunt ut labore et dolore magna aliqua. Quis ipsum suspendisse ultrices gravida. Risus commodo viverra maecenas accumsan lacus vel facilisis. Lorem ipsum dolor sit amet, consectetur adipiscing elit, sed do eiusmod tempor incididunt ut labore et dolore magna aliqua. Quis ipsum suspendisse ultrices gravida. Risus commodo viverra maecenas accumsan lacus vel facilisis.</p>
        <p>Lorem ipsum dolor sit amet, consectetur adipiscing elit, sed do eiusmod tempor incididunt ut labore et dolore magna aliqua. Quis ipsum suspendisse ultrices gravida. Risus commodo viverra maecenas accumsan lacus vel facilisis. Lorem ipsum dolor sit amet, consectetur adipiscing elit, sed do eiusmod tempor incididunt ut labore et dolore magna aliqua. Quis ipsum suspendisse ultrices gravida. Risus commodo viverra maecenas accumsan lacus vel facilisis. Lorem ipsum dolor sit amet, consectetur adipiscing elit, sed do eiusmod tempor incididunt ut labore et dolore magna aliqua. Quis ipsum suspendisse ultrices gravida. Risus commodo viverra maecenas accumsan lacus vel facilisis.</p>
      </div>
    </section>

    <div class="spine-title distressed">Iron Silence?</div>
    <div class="spine-author">OWEN FRICK</div>

    <section class="front">
      <h1 class="front-title">
        <span class="front-title-line1 distressed">Iron</span>
        <span class="front-title-line2 distressed">Silence?</span>
      </h1>
      <div class="cover-art" role="img" aria-label="Line drawing of four angry stick figures pointing at a worried figure beneath a tangled scribble of thoughts"></div>
      <div class="ground-line"></div>
      <p class="front-subtitle">How the Harbour Works Department Condones<br>Bullying &amp; Ruins Lives</p>
      <p class="front-author">OWEN FRICK</p>
    </section>
  </main>
</body>
</html>
```